Anzeigengestaltung - Lurik Pflegedienst
Zielgruppe
Moin, wir sind Spezialist für die Invasive und nicht-invasive Heimbeatmung seit nun mehr 20 Jahren. Gegründet wurde der Dienst aus eigener Betroffenheit. Unsere Website wird zur Zeit überarbeitet: lurik-pflegedienst.de
Wir suchen in und um Hamburg Pflegefach- und Hilfskräfte. Wir suchen sowohl junge als auch ältere Fachkräfte. Wir wollen unsere Stellenanzeigen ausweiten und suchen nun nach einer Grafik für tauschmarkt-Inserate und eine Ausgestaltung für der Stellenanzeige für stellwerk.com
Aufgabenstellung
Wir wünschen uns eine Anzeige, die nicht nach Krankenhaus aussieht oder Menschen mit 'steriler' Arbeitsbekleidung darstellt. Wir arbeiten hauptsächlich mit einem Blauton unser Logo ist s/w. Der Name des Unternehmens gründet sich auf die Erzählung aus dem Buch Lurik aus dem Alten Testament der Bibel. Das Logo stellt einen Fisch dar.
Unsere Mitarbeiter sind bei den Menschen vor Ort und unterstützen sie im Alltag. Wir versuchen ihnen ein uneingeschränktes Leben trotz ihrer Benachteiligung zu geben. Dazu gehören auch Ausflüge und Freizeitgestaltung. Eine Notfallsituation kann jederzeit eintreffen und dazu haben wir geschultes Personal vor Ort.
Wir haben noch keine Erfahrungen mit stellwerk gemacht, jedoch mit tauschmarkt-Inserate. Dazu anbei ein Link unsers Profils mit allen aktuellen Anzeigen: https://www.tauschmarkt-inserate.de/s-bestandsliste.html?userId=58140276
Wunsch:
- Eine Grafik für tauschmarkt-Inserate
- Stellengesuch für stellwerk auf Grundlage unserer bisherigen Anzeigen von tauschmarkt-Inserate
Edit:
Maße & Format für Kleinanzeigen: https://themen.tauschmarkt-inserate.de/hilfe/technische-fragen/bilderupload/?device=desktop
Der Inhalt der Anzeige soll sich in der Grafik widerspiegeln aber nur mit ein paar 'Highlights' - ich denke es wäre hilfreich diese noch zu benennen (folgt). Das Bild wollen wir dann für beide Portale nutzen. Es geht also mehr um die Grafik als um ein klassisches Stellengesuch in Zeitschriften. Die Grafik soll, wie jede andere, zum lesen der Stellenanzeige anregen.
Wir sind gespannt.

```html
<!DOCTYPE html>
<html lang="de">
<head>
<meta charset="utf-8">
<title>Lurik Pflegedienst – Stellenanzeige</title>
<link rel="stylesheet" href="https://fonts.googleapis.com/css2?family=Open+Sans:wght@400;600;700&display=swap">
<style>
  :root {
    --canvas-bg: #e4e5e7;
    --ink: #1c1c1c;
    --sky-top: #ffffff;
    --sky-low: #e3eef7;
    --wave-light: #9fcbe9;
    --sea-mid: #3d8cc9;
    --sea-deep: #0f4f8c;
    --headline: #5b8ab0;
    --white: #ffffff;
    --band: rgba(60, 70, 82, 0.82);
  }
  * { margin: 0; padding: 0; box-sizing: border-box; }
  html, body { width: 1200px; height: 740px; overflow: hidden; }
  body {
    background: var(--canvas-bg);
    font-family: "Open Sans", sans-serif;
    position: relative;
  }
  .job-ad {
    position: absolute;
    left: 135px; top: 20px;
    width: 930px; height: 700px;
    overflow: hidden;
    background: var(--sky-top);
    box-shadow: 0 6px 24px rgba(0,0,0,0.12);
  }
  .ad-backdrop {
    position: absolute; inset: 0;
    background: linear-gradient(180deg,
      var(--sky-top) 0%,
      var(--sky-low) 30%,
      var(--wave-light) 37%,
      var(--sea-mid) 52%,
      var(--sea-deep) 100%);
  }
  .brand {
    position: absolute; left: 50px; top: 70px;
    display: flex; align-items: center; gap: 18px;
  }
  .brand-dot {
    width: 70px; height: 70px; border-radius: 50%;
    background: var(--ink);
  }
  .brand-name {
    font-weight: 600; font-size: 44px; color: var(--ink);
    line-height: 1.05;
  }
  .service-claim {
    position: absolute; left: 528px; top: 56px; width: 390px;
    font-size: 30px; line-height: 1.22; color: var(--ink);
  }
  .service-claim strong { font-weight: 700; }
  .headline {
    position: absolute; left: 0; right: 0; top: 340px;
    text-align: center;
    font-weight: 700; font-size: 56px; color: var(--headline);
    letter-spacing: 0.5px;
  }
  .values {
    position: absolute; left: 0; right: 0; top: 420px;
    text-align: center;
    font-size: 37px; color: var(--white);
    letter-spacing: 0.4px;
  }
  .hiring-box {
    position: absolute; left: 78px; top: 494px;
    width: 786px; height: 60px;
    background: var(--white);
    display: flex; align-items: center; justify-content: center;
    font-size: 31px; color: #2b2b2b; letter-spacing: 0.5px;
  }
  .contact-band {
    position: absolute; left: 0; right: 0; bottom: 0; height: 84px;
    background: var(--band);
    display: flex; align-items: center; justify-content: center;
    font-size: 33px; color: var(--white); letter-spacing: 0.3px;
  }
</style>
</head>
<body>
  <article class="job-ad">
    <div class="ad-backdrop" role="img" aria-label="Meeresoberfläche mit Wellen und Blick unter Wasser in Blautönen"></div>

    <div class="brand">
      <span class="brand-dot"></span>
      <span class="brand-name">Lurik<br>Pflegedienst</span>
    </div>

    <p class="service-claim">
      Ihr Intensiv- und Beatmungspflegedienst
      <strong>für den Landkreis Harburg und Umgebung.</strong>
    </p>

    <h1 class="headline">Pflege bei Lurik ist</h1>
    <p class="values">Teamwork | Leidenschaft | Verantwortung</p>
    <p class="hiring-box">Wir suchen Verstärkung für unseren Pflegedienst</p>

    <footer class="contact-band">info@lurik-pflegedienst.de | www.lurik-pflegedienst.de</footer>
  </article>
</body>
</html>
```